I need the Scorecard I've developed for my staff to be produced into a visually engaging piece that will encourage the staff to utilize it on a daily basis. I'm thinking it could be 5x7 in size so that it isn't too cumbersome, but I'm open to different layouts.
I have multiple other departments that will need Scorecards created for them as well, but each one will contain task specific questions for each department.

```html
<!DOCTYPE html>
<html lang="en">
<head>
<meta charset="utf-8">
<title>Receptionist Daily Excellence Scorecard</title>
<link href="https://fonts.googleapis.com/css2?family=Poppins:wght@400;500;600;700&display=swap" rel="stylesheet">
<style>
:root{
  --bg:#a7a7a7;
  --paper:#ffffff;
  --plum:#5b1a68;
  --violet:#7d2b96;
  --purple:#8a2aa6;
  --bright:#9b1dc0;
  --rose:#d23a63;
  --ink:#1f1f24;
  --row:#e7e7ea;
  --rule:#c9c9cd;
  --head-grad:linear-gradient(90deg,#7b2f98 0%,#a5357f 50%,#d33a60 100%);
}
*{margin:0;padding:0;box-sizing:border-box}
html,body{width:1200px;height:1200px;overflow:hidden;background:var(--bg)}
body{position:relative;font-family:'Poppins',sans-serif;color:var(--ink)}
.page{position:absolute;top:209px;width:535px;height:749px;background:var(--paper);overflow:hidden}
.page--scorecard{left:48px}
.page--summary{left:617px}
.page__band{position:absolute;left:0;top:0;width:100%;height:116px;background:var(--head-grad)}
.page__card{position:absolute;left:26px;top:65px;width:483px;height:100px;background:var(--paper);border-radius:16px 16px 0 0}
.page__title{position:absolute;left:0;right:0;top:28px;text-align:center;color:#fff;font-weight:700;font-size:20px;letter-spacing:-.1px;white-space:nowrap}
.page__foot{position:absolute;left:0;bottom:0;width:100%;height:9px;background:#9c2f7e}
.abs{position:absolute}
.field-label{font-size:9px;font-weight:500}
.field-line{height:1px;background:#b9b9bd}
.scale{position:absolute;left:41px;top:129px;width:453px;height:32px;display:flex;border-radius:5px;overflow:hidden;color:#fff;font-size:10px;line-height:1.1}
.scale__cell{display:flex;align-items:center;padding-left:15px}
.scale__cell:nth-child(1){width:138px;background:var(--plum)}
.scale__cell:nth-child(2){width:107px;background:#6e2283}
.scale__cell:nth-child(3){width:105px;background:#8524a0}
.scale__cell:nth-child(4){width:103px;background:var(--bright);justify-content:center;padding:0}
.section-title{position:absolute;display:flex;align-items:center;gap:5px;font-size:8.6px;font-weight:700;white-space:nowrap}
.section-title__num{width:15px;height:15px;border-radius:50%;background:var(--plum);color:#fff;font-size:8px;display:flex;align-items:center;justify-content:center}
.task-table{position:absolute;width:212px}
.task-table__head{display:flex;gap:4px;height:22px}
.task-table__head div{color:#fff;font-size:7px;font-weight:500;display:flex;align-items:center;justify-content:center;text-align:center;line-height:1;border-radius:4px 4px 0 0}
.th-task{width:88px;background:var(--plum);font-weight:600!important}
.th-rate{width:58px;background:var(--violet)}
.th-notes{width:58px;background:var(--rose)}
.task-table__body{border:1px solid var(--rule);border-top:none;border-radius:0 0 7px 7px;overflow:hidden}
.task-row{display:flex;font-size:7.2px;line-height:1.22}
.task-row:nth-child(odd){background:var(--row)}
.task-row div{border-right:1px solid var(--rule)}
.task-row div:last-child{border-right:none}
.tr-task{width:90px;padding-left:10px;display:flex;align-items:center}
.tr-rate{width:62px}
.tr-notes{flex:1}
.status{position:absolute;left:84px;display:flex;align-items:center;gap:6px;font-size:9.6px;white-space:nowrap}
.status__ring{width:12px;height:12px;border-radius:50%;border:2px solid}
.status b{font-weight:600}
.divider{position:absolute;left:40px;width:457px;height:1px;background:#cfcfd3}
.heading{position:absolute;left:41px;font-size:12px;font-weight:700;color:var(--violet);white-space:nowrap}
.question{position:absolute;left:41px;font-size:10.5px;font-weight:500;white-space:nowrap}
.question--light{font-weight:400}
.answer-box{position:absolute;left:41px;width:456px;border:1px solid #cfcfd3;background:#fff}
.sign{position:absolute;top:687px;width:128px;border-top:1px solid #cfcfd3;text-align:center;font-size:8.4px;font-weight:600;padding-top:5px}
</style>
</head>
<body>

<section class="page page--scorecard">
  <div class="page__band"></div>
  <h1 class="page__title">RECEPTIONIST DAILY EXCELLENCE SCORECARD</h1>
  <div class="page__card"></div>

  <span class="abs field-label" style="left:41px;top:81px">Name:</span>
  <div class="abs field-line" style="left:77px;top:91px;width:175px"></div>
  <span class="abs field-label" style="left:272px;top:81px">Date:</span>
  <div class="abs field-line" style="left:302px;top:91px;width:191px"></div>
  <span class="abs field-label" style="left:41px;top:104px">Location:</span>
  <div class="abs field-line" style="left:87px;top:113px;width:406px"></div>

  <div class="scale">
    <div class="scale__cell">Please rate yourself<br>for each task</div>
    <div class="scale__cell">1 = Needs<br>Improvement</div>
    <div class="scale__cell">3 = Meets<br>Expectations</div>
    <div class="scale__cell">5 = Excellent</div>
  </div>

  <!-- Section 1 -->
  <div class="section-title" style="left:41px;top:171px"><span class="section-title__num">1</span>CALL HANDLING &amp; FIRST CALL INTAKE</div>
  <div class="task-table" style="left:41px;top:193px">
    <div class="task-table__head"><div class="th-task">Task</div><div class="th-rate">Self-Rating<br>(1-5)</div><div class="th-notes">Notes /<br>Issues</div></div>
    <div class="task-table__body">
      <div class="task-row" style="height:31px"><div class="tr-task">Answered 90%+<br>calls within 3 rings</div><div class="tr-rate"></div><div class="tr-notes"></div></div>
      <div class="task-row" style="height:35px"><div class="tr-task">Maintained<br>empathy and<br>professionalism</div><div class="tr-rate"></div><div class="tr-notes"></div></div>
      <div class="task-row" style="height:35px"><div class="tr-task">Accurately<br>completed all First<br>Call fields</div><div class="tr-rate"></div><div class="tr-notes"></div></div>
      <div class="task-row" style="height:29px"><div class="tr-task">Worked within<br>Receptionist role</div><div class="tr-rate"></div><div class="tr-notes"></div></div>
    </div>
  </div>

  <!-- Section 4 -->
  <div class="section-title" style="left:282px;top:171px"><span class="section-title__num">4</span>CLOTHING &amp; FLOWERS</div>
  <div class="task-table" style="left:282px;top:193px">
    <div class="task-table__head"><div class="th-task">Task</div><div class="th-rate">Self-Rating<br>(1-5)</div><div class="th-notes">Notes /<br>Issues</div></div>
    <div class="task-table__body">
      <div class="task-row" style="height:25px"><div class="tr-task">Answered 90%+<br>calls within 3 rings</div><div class="tr-rate"></div><div class="tr-notes"></div></div>
      <div class="task-row" style="height:25px"><div class="tr-task">Family contact<br>noted on sheet</div><div class="tr-rate"></div><div class="tr-notes"></div></div>
      <div class="task-row" style="height:25px"><div class="tr-task">Floral deliveries<br>logged</div><div class="tr-rate"></div><div class="tr-notes"></div></div>
      <div class="task-row" style="height:27px"><div class="tr-task">Concerns<br>communicated<br>to Care Center</div><div class="tr-rate"></div><div class="tr-notes"></div></div>
      <div class="task-row" style="height:27px"><div class="tr-task">Flower placement<br>verified</div><div class="tr-rate"></div><div class="tr-notes"></div></div>
    </div>
  </div>

  <!-- Section 2 -->
  <div class="section-title" style="left:41px;top:356px"><span class="section-title__num">2</span>CALL MANAGEMENT DURING BUSY TIMES</div>
  <div class="task-table" style="left:41px;top:377px">
    <div class="task-table__head"><div class="th-task">Task</div><div class="th-rate">Self-Rating<br>(1-5)</div><div class="th-notes">Notes /<br>Issues</div></div>
    <div class="task-table__body">
      <div class="task-row" style="height:32px"><div class="tr-task">Prioritized urgent vs.<br>non-urgent calls</div><div class="tr-rate"></div><div class="tr-notes"></div></div>
      <div class="task-row" style="height:34px"><div class="tr-task">Hold times<br>under 1 minute</div><div class="tr-rate"></div><div class="tr-notes"></div></div>
      <div class="task-row" style="height:35px"><div class="tr-task">Logged all<br>calls</div><div class="tr-rate"></div><div class="tr-notes"></div></div>
      <div class="task-row" style="height:30px"><div class="tr-task">Requested help if<br>overwhelmed</div><div class="tr-rate"></div><div class="tr-notes"></div></div>
    </div>
  </div>

  <!-- Section 5 -->
  <div class="section-title" style="left:282px;top:356px"><span class="section-title__num">5</span>DEATH CERTIFICATES</div>
  <div class="task-table" style="left:282px;top:377px">
    <div class="task-table__head"><div class="th-task">Task</div><div class="th-rate">Self-Rating<br>(1-5)</div><div class="th-notes">Notes /<br>Issues</div></div>
    <div class="task-table__body">
      <div class="task-row" style="height:32px"><div class="tr-task">Verified recipient<br>ID &amp; relationship</div><div class="tr-rate"></div><div class="tr-notes"></div></div>
      <div class="task-row" style="height:34px"><div class="tr-task">Confirmed correct<br>documents<br>enclosed</div><div class="tr-rate"></div><div class="tr-notes"></div></div>
      <div class="task-row" style="height:30px"><div class="tr-task">Recipient signed<br>the DC logbook</div><div class="tr-rate"></div><div class="tr-notes"></div></div>
      <div class="task-row" style="height:35px"><div class="tr-task">Suggested<br>proofreading<br>before leaving</div><div class="tr-rate"></div><div class="tr-notes"></div></div>
    </div>
  </div>

  <!-- Section 3 -->
  <div class="section-title" style="left:41px;top:543px"><span class="section-title__num">3</span>SCHEDULING ACCURACY</div>
  <div class="task-table" style="left:41px;top:564px">
    <div class="task-table__head"><div class="th-task">Task</div><div class="th-rate">Self-Rating<br>(1-5)</div><div class="th-notes">Notes /<br>Issues</div></div>
    <div class="task-table__body">
      <div class="task-row" style="height:40px"><div class="tr-task">Answered 90%+<br>calls within 3 rings</div><div class="tr-rate"></div><div class="tr-notes"></div></div>
      <div class="task-row" style="height:44px"><div class="tr-task">Cross-checked<br>with Red Book</div><div class="tr-rate"></div><div class="tr-notes"></div></div>
      <div class="task-row" style="height:46px"><div class="tr-task">Entered<br>manifold info<br>promptly</div><div class="tr-rate"></div><div class="tr-notes"></div></div>
    </div>
  </div>

  <!-- Section 6 -->
  <div class="section-title" style="left:282px;top:543px"><span class="section-title__num">6</span>ROUTING &amp; MESSAGES</div>
  <div class="task-table" style="left:283px;top:564px">
    <div class="task-table__head"><div class="th-task">Task</div><div class="th-rate">Self-Rating<br>(1-5)</div><div class="th-notes">Notes /<br>Issues</div></div>
    <div class="task-table__body">
      <div class="task-row" style="height:40px"><div class="tr-task">Calls routed<br>appropriately</div><div class="tr-rate"></div><div class="tr-notes"></div></div>
      <div class="task-row" style="height:44px"><div class="tr-task">Messages<br>included all<br>required info</div><div class="tr-rate"></div><div class="tr-notes"></div></div>
      <div class="task-row" style="height:46px"><div class="tr-task">Delivered<br>95%+ messages<br>in 30 min</div><div class="tr-rate"></div><div class="tr-notes"></div></div>
    </div>
  </div>

  <div class="page__foot"></div>
</section>

<section class="page page--summary">
  <div class="page__band"></div>
  <h1 class="page__title">DAILY STATUS SUMMARY (CIRCLE ONE)</h1>
  <div class="page__card"></div>

  <div class="status" style="top:82px"><span class="status__ring" style="border-color:var(--plum)"></span><span><b>Excellent</b> – All key duties completed, proactive, calm under pressure</span></div>
  <div class="status" style="top:106px"><span class="status__ring" style="border-color:var(--purple)"></span><span><b>Satisfactory</b> – Most duties completed, minor follow-up needed</span></div>
  <div class="status" style="top:129px"><span class="status__ring" style="border-color:var(--rose)"></span><span><b>Needs Support</b> – Missed urgent duties, accuracy or stress issues</span></div>

  <div class="divider" style="top:163px"></div>

  <div class="heading" style="top:177px">DAILY REFLECTION</div>
  <div class="question" style="top:200px">What went well today?</div>
  <div class="answer-box" style="top:219px;height:32px"></div>
  <div class="question" style="top:257px">Any issues or barriers to note?</div>
  <div class="answer-box" style="top:275px;height:32px"></div>
  <div class="question" style="top:320px">Support needed from supervisor?</div>
  <div class="answer-box" style="top:339px;height:32px"></div>

  <div class="heading" style="top:387px">STARS &amp; FLAGS (SUPERVISOR USE ONLY)</div>
  <div class="question question--light" style="top:404px">Stars (Excellence or above-and-beyond moments)</div>
  <div class="answer-box" style="top:426px;height:35px"></div>
  <div class="question question--light" style="top:476px"><span style="color:var(--violet);font-weight:700;font-size:12px">FLAGS</span> (Concerns needing follow-up/coaching)</div>
  <div class="answer-box" style="top:499px;height:32px"></div>

  <div class="heading" style="top:558px">MANAGER'S OVERALL RATING</div>
  <div class="question question--light" style="top:576px">(Manager: Please rate overall performance on a 1-5 scale)</div>
  <div class="question question--light" style="top:591px;font-size:8.6px">Manager Overall Rating (1-5)</div>
  <div class="answer-box" style="top:618px;height:35px"></div>

  <div class="sign" style="left:41px">RECEPTIONIST SIGNATURE</div>
  <div class="sign" style="left:204px">SUPERVISOR SIGNATURE</div>
  <div class="sign" style="left:366px">DATE</div>

  <div class="page__foot"></div>
</section>

</body>
</html>
```